Medical VIP club - small design

Please read the specs in a design brief attached. Also we don't have logo in a Vector format and attaching the only version we have.

Industry/Entity Type

Club

```html
<!DOCTYPE html>
<html lang="en">
<head>
<meta charset="utf-8">
<title>Veridan — Medical VIP Club</title>
<link href="https://fonts.googleapis.com/css2?family=Arimo:wght@400;700&family=PT+Sans:ital,wght@0,400;1,400;1,700&display=swap" rel="stylesheet">
<style>
:root{
  --topbar:#231815;
  --orange:#f39a1e;
  --orange-light:#fbc25a;
  --accent:#f08a2c;
  --band:#3a3a3a;
  --ink:#5a5a5a;
  --ink-dark:#444;
  --ink-soft:#777;
  --page:#f4f4f4;
  --white:#fff;
  --blue:#a9c0ee;
  --brand-blue:#1f5fb8;
  --fb:#3b5998;
  --footer:#e9e9e9;
}
*{margin:0;padding:0;box-sizing:border-box}
html,body{width:1088px;height:1200px;overflow:hidden}
body{position:relative;background:var(--page);font-family:Arimo,Arial,sans-serif;color:var(--ink)}
.abs{position:absolute}
.topbar{left:0;top:0;width:1088px;height:40px;background:var(--topbar)}
.login{left:378px;top:4px;color:var(--white)}
.login h3{font-size:12px;font-weight:700}
.login p{font-size:7px;line-height:9px;width:280px;margin-top:1px}
.search{left:806px;top:11px;width:134px;height:20px;border-radius:10px;background:var(--white);border:1px solid #bbb;font-size:8px;color:#888;padding:5px 10px}
.search svg{position:absolute;right:7px;top:3px}
.hero{left:0;top:44px;width:1088px;height:262px;background:linear-gradient(180deg,var(--orange-light),var(--orange));border-top:2px solid #fff}
.hero-photo{left:358px;top:44px;width:442px;height:262px;background:linear-gradient(100deg,#e9a64a,#d98d2c 55%,#f6b64a)}
.band{left:0;top:306px;width:1088px;height:22px;background:var(--band)}
.fb-connect{left:820px;top:310px;width:92px;height:15px;background:var(--fb);color:#fff;font-size:8px;font-weight:700;display:flex;align-items:center;gap:4px;padding-left:3px}
.fb-connect i{width:9px;height:9px;background:#fff;display:block}
.share-dot{left:924px;top:298px;width:22px;height:22px;border-radius:50%;background:#39a6e4}
.sidebar{left:139px;top:0;width:219px;height:320px;background:var(--white);border-radius:0 0 10px 10px;box-shadow:0 2px 4px rgba(0,0,0,.2)}
.logo-cap{left:136px;top:0;width:227px;height:110px;background:var(--white);border-radius:0 0 50% 50%/0 0 30% 30%;box-shadow:0 4px 6px rgba(0,0,0,.25)}
.brand{left:158px;top:36px;width:190px;display:flex;align-items:center;gap:6px;font-size:34px;font-weight:700;color:var(--brand-blue)}
.brand i{width:20px;height:20px;border-radius:50%;background:var(--brand-blue);display:block}
.menu{left:150px;top:132px;width:196px}
.menu a{display:flex;justify-content:space-between;align-items:center;height:32px;margin-bottom:10px;padding:0 8px 0 19px;border:1px solid #ccc;border-radius:6px;background:linear-gradient(#fafafa,#e6e6e6);font-size:11px;font-weight:700;color:var(--ink-dark);text-decoration:none}
.services{left:137px;top:330px;width:815px;height:152px;display:flex;background:linear-gradient(#fff,#f0f0f0);box-shadow:0 3px 4px rgba(0,0,0,.12)}
.service{flex:1;border-left:1px solid #a6b8dc;padding:8px 15px;position:relative}
.service:last-child{border-right:1px solid #a6b8dc}
.service h4{font-size:14px;font-weight:700;color:var(--ink-dark);line-height:18px}
.service .icon{position:absolute;left:50%;top:52px;width:58px;height:58px;margin-left:-29px;border-radius:8px;background:linear-gradient(#d9d9d9,#b7b7b7)}
h2.section{font-size:16px;font-weight:700;color:var(--ink-dark)}
.rule{height:5px;background:var(--accent)}
.lead{font-size:11px;font-weight:700;line-height:14px;color:#666}
.body{font-size:9.5px;line-height:11.7px;color:#666}
.news h5{font-size:11px;font-weight:700;color:var(--ink-dark)}
.subscribe h3{font-family:"PT Sans",sans-serif;font-style:italic;font-weight:700;font-size:19px;color:#555}
.subscribe small{font-family:"PT Sans",sans-serif;font-size:9px;display:block}
.field{width:198px;height:24px;border:1px solid #aaa;background:#fff;font-family:"PT Sans",sans-serif;font-size:9px;padding:5px 7px;position:relative;margin-top:4px}
.field i{position:absolute;right:6px;top:4px;width:14px;height:14px;border-radius:50%;background:#f07a1a}
.apply{left:825px;top:820px;width:65px;height:26px;border-radius:6px;background:linear-gradient(#b9d4f7,#5d93dc);border:1px solid #4b7cc0;color:#fff;font-family:"PT Sans",sans-serif;font-weight:700;font-size:14px;text-align:center;line-height:24px}
.gallery{left:164px;top:879px;display:flex;gap:4px}
.gallery div{width:148px;height:99px}
.arrow{width:18px;height:18px;border-radius:50%;border:1px solid #aaa;background:linear-gradient(#fff,#ddd)}
.arrow svg{display:block;margin:4px}
.footer{left:0;top:1010px;width:1088px;height:170px;background:var(--footer);border-top:2px solid #ccc}
.footer h4{font-family:"PT Sans",sans-serif;font-style:italic;font-weight:700;font-size:14px;color:#8a8a8a}
.footer p{font-size:9.5px;line-height:11.6px;color:#777}
.social{display:flex;gap:4px;margin-top:5px}
.social i{width:26px;height:26px;border-radius:5px;background:#4a4a4a;display:block}
.bottom{left:0;top:1180px;width:1088px;height:20px;background:linear-gradient(#d8d8d8,#eee);font-size:9.5px;color:#777;padding:3px 0 0 151px}
</style>
</head>
<body>
<div class="abs topbar"></div>
<div class="abs login"><h3>Register / Log In</h3><p>Lorem ipsum dolor sit amet, consectetuer adipiscing elit. Aenean commodo ligula eget dolor.</p></div>
<div class="abs search">Search<svg width="12" height="12" viewBox="0 0 12 12"><circle cx="5" cy="5" r="3.6" fill="none" stroke="#555" stroke-width="1.8"/><line x1="7.6" y1="7.6" x2="11" y2="11" stroke="#555" stroke-width="2"/></svg></div>

<div class="abs hero"></div>
<div class="abs hero-photo" role="img" aria-label="Photo of a smiling doctor and two nurses in a bright clinic"></div>
<div class="abs band"></div>
<div class="abs fb-connect"><i></i>Connect with us</div>
<div class="abs share-dot"></div>

<div class="abs sidebar"></div>
<div class="abs logo-cap"></div>
<div class="abs brand"><i></i>Veridan</div>
<nav class="abs menu">
  <a href="#">ABOUT US<svg width="18" height="18" viewBox="0 0 18 18"><circle cx="9" cy="9" r="8" fill="#ddd" stroke="#888"/><path d="M7.5 5.5 11 9 7.5 12.5" fill="none" stroke="#555" stroke-width="1.6"/></svg></a>
  <a href="#">VIP CLUB<svg width="18" height="18" viewBox="0 0 18 18"><circle cx="9" cy="9" r="8" fill="#ddd" stroke="#888"/><path d="M7.5 5.5 11 9 7.5 12.5" fill="none" stroke="#555" stroke-width="1.6"/></svg></a>
  <a href="#">PACKAGES AND PRICES<svg width="18" height="18" viewBox="0 0 18 18"><circle cx="9" cy="9" r="8" fill="#ddd" stroke="#888"/><path d="M7.5 5.5 11 9 7.5 12.5" fill="none" stroke="#555" stroke-width="1.6"/></svg></a>
  <a href="#">CONTACT US<svg width="18" height="18" viewBox="0 0 18 18"><circle cx="9" cy="9" r="8" fill="#ddd" stroke="#888"/><path d="M7.5 5.5 11 9 7.5 12.5" fill="none" stroke="#555" stroke-width="1.6"/></svg></a>
</nav>

<section class="abs services">
  <div class="service"><h4>Emergeny Services Plan Covers.</h4><div class="icon" role="img" aria-label="Heart monitor icon"></div></div>
  <div class="service"><h4>Transportation Services</h4><div class="icon" role="img" aria-label="Ambulance icon"></div></div>
  <div class="service"><h4>Hotel Services</h4><div class="icon" role="img" aria-label="Hospital building icon"></div></div>
  <div class="service"><h4>Variety of Doctors</h4><div class="icon" role="img" aria-label="Doctor icon"></div></div>
  <div class="service"><h4>Become a Member</h4><div class="icon" role="img" aria-label="Medical clipboard icon"></div></div>
</section>

<div class="abs" style="left:154px;top:500px"><h2 class="section">Welcome to our website</h2></div>
<div class="abs rule" style="left:137px;top:521px;width:260px"></div>
<div class="abs" style="left:154px;top:537px;width:470px">
  <p class="lead">Lorem ipsum dolor sit amet, consectetuer adipiscing elit. Aenean commodo ligula eget dolor. Aenean massa.</p>
  <p class="body" style="margin-top:6px">Aenean commodo ligula eget dolor. Aenean massa. Cum sociis natoque penatibus et magnis dis parturient montes, nascetur ridiculus mus. Donec quam felis, ultricies nec, pellentesque eu, pretium quis, sem.</p>
  <p class="body" style="margin-top:11px">Nulla consequat massa quis enim. Donec pede justo, fringilla vel, aliquet nec, vulputate eget, arcu. In enim justo, rhoncus ut, imperdiet a, venenatis vitae, justo. Nullam dictum felis eu pede mollis pretium. Integer tincidunt. Cras dapibus. Vivamus elementum semper nisi. Aenean vulputate eleifend tellus.</p>
</div>

<div class="abs" style="left:154px;top:671px"><h2 class="section">Lorenm Ipsum Dolor</h2></div>
<div class="abs rule" style="left:136px;top:693px;width:247px"></div>
<div class="abs body" style="left:166px;top:710px;width:200px">Lorem ipsum dolor sit amet, consectetuer adipiscing elit. Aenean commodo ligula eget dolor.<br><span style="display:block;margin-top:6px">Lorem ipsum dolor sit amet, consectetuer adipiscing elit. Aenean commodo ligula eget dolor.</span></div>
<div class="abs body" style="left:415px;top:709px;width:200px">Lorem ipsum dolor sit amet, consectetuer adipiscing elit. Aenean commodo ligula eget dolor.<br><span style="display:block;margin-top:6px">Lorem ipsum dolor sit amet, consectetuer adipiscing elit. Aenean commodo ligula eget dolor.</span></div>

<div class="abs" style="left:691px;top:500px"><h2 class="section">Latest News</h2></div>
<div class="abs rule" style="left:691px;top:522px;width:261px"></div>
<div class="abs news" style="left:691px;top:537px;width:245px">
  <h5>Jhon Doe</h5><p class="body">Posted on 12-01-2012</p>
  <p class="body" style="margin-top:7px">Lorem ipsum dolor sit amet, consectetuer adipiscing elit. Aenean commodo ligula eget dolor. Aenean massa. Cum sociis natoque penatibus et magnis dis parturient montes, nascetur ridiculus mus.</p>
  <h5 style="margin-top:9px">Jhon Doe</h5><p class="body">Posted on 12-01-2012</p>
  <p class="body" style="margin-top:7px">Lorem ipsum dolor sit amet, consectetuer adipiscing elit. Aenean commodo ligula eget dolor. Aenean massa. Cum sociis natoque penatibus et magnis dis parturient montes, nascetur ridiculus mus.</p>
</div>
<div class="abs" style="left:882px;top:721px;font-size:9.5px;font-weight:700;color:#777">read more</div>

<div class="abs subscribe" style="left:691px;top:751px">
  <h3>Subscribe us</h3>
  <small>Exclusive deals delivered every day</small>
  <div class="field">enter your email here<i></i></div>
  <small style="margin-top:3px">unsubscribe us click here</small>
</div>
<div class="abs apply">Appy</div>

<div class="abs" style="left:171px;top:834px"><h2 class="section">See Our Service</h2></div>
<div class="abs" style="left:137px;top:860px;width:815px;height:6px;background:var(--blue)"></div>
<div class="abs arrow" style="left:141px;top:919px"><svg width="8" height="8" viewBox="0 0 8 8"><path d="M5.5 1 2.5 4 5.5 7" fill="none" stroke="#555" stroke-width="1.5"/></svg></div>
<div class="abs gallery">
  <div role="img" aria-label="Hospital emergency entrance" style="background:linear-gradient(#a7b7c9,#b88b78 60%,#7b5a4c)"></div>
  <div role="img" aria-label="Flight attendant serving a passenger" style="background:linear-gradient(120deg,#ddd,#8c8c8c 55%,#2e2e2e)"></div>
  <div role="img" aria-label="Hotel room with beds" style="background:linear-gradient(#f1e6a3,#d9a650 60%,#9a6a2a)"></div>
  <div role="img" aria-label="Flight attendant serving a passenger" style="background:linear-gradient(120deg,#ddd,#8c8c8c 55%,#2e2e2e)"></div>
  <div role="img" aria-label="Hotel room with beds" style="background:linear-gradient(#f1e6a3,#d9a650 60%,#9a6a2a)"></div>
</div>
<div class="abs arrow" style="left:928px;top:921px"><svg width="8" height="8" viewBox="0 0 8 8"><path d="M2.5 1 5.5 4 2.5 7" fill="none" stroke="#555" stroke-width="1.5"/></svg></div>
<div class="abs" style="left:164px;top:981px;font-size:7.5px;color:#666">Click images to enlarge</div>

<footer class="abs footer">
  <div class="abs" style="left:151px;top:10px;width:190px">
    <h4>More About US</h4>
    <p style="margin-top:3px">Lorem ipsum dolor sit amet, consectetuer adipiscing elit. Aenean commodo ligula eget dolor. Aenean massa. Cum sociis natoque penatibus et magnis dis</p>
    <h4 style="margin-top:7px;margin-left:-1px">Lorem Ipsum</h4>
    <p style="font-family:'PT Sans',sans-serif;font-size:9px;line-height:11.6px;margin-left:3px">insert Link<br>insert Link<br>insert Link<br>insert Link<br>insert Link</p>
  </div>
  <div class="abs" style="left:424px;top:9px;width:130px">
    <h4>Why Veridan</h4>
    <p style="margin-top:3px">Lorem ipsum dolor sit amet, consectetuer adipiscing elit. Aenean commodo ligula eget dolor. Aenean massa. Cum sociis natoque penatibus et magnis dis</p>
  </div>
  <div class="abs" style="left:632px;top:7px;width:135px">
    <h4>Contact Us</h4>
    <p style="margin-top:5px;margin-left:3px">Lorem Ipsum Rd 2010 California.<br>6411</p>
    <p style="margin-top:11px;margin-left:3px">Phone&nbsp; 555-0142 778<br>Email :<br>hello@veridan-club.com</p>
  </div>
  <div class="abs" style="left:838px;top:24px;display:flex;align-items:center;gap:4px;font-size:20px;font-weight:700;color:#666"><i style="width:12px;height:12px;border-radius:50%;background:#666;display:block"></i>Veridan</div>
  <div class="abs" style="left:834px;top:66px">
    <p>Stay Connected to us on :</p>
    <div class="social"><i></i><i></i><i></i><i></i></div>
  </div>
</footer>
<div class="abs bottom">Copyright veridan-club.com All Right Reserved 2011</div>
</body>
</html>
```